The Bright Meadow Foundation

This is a non profit . We are a 501(c)(3) charitable organization in the United States. The organization is a volunteer based group providing basic healthcare to those living in underserved rural areas around the world. I have attached a brochure that provides some information about the organization. We are looking for a basic 5 page web page Page 1 Photos that fade into the next x 3 with mission statementPage 2 About us - details about bright meadow foundation. also introducing our Founders of the organization. Marina Kellet, M.D. Dorla Penn , FNP, Rosa Tembley, FNP, Wade Marlow. ( will provide you info on each.Page 3 Projects coming up and futurePage 4 Get involved - Give a donation, Volunteer, Corporate supportPage 5 Support us and contact us with a message box.We mainly work in South America but anticipate trave to South Africa in the near future. Colors bright with emphasis on Reds and Purples. I have attached some photos and ideas. You can use or not use ok to use something similar if you so like

Target Market(s)

People interested in volunteering time or money to overseas medical work. NOT a religious base

Coding

Coded - Design and coding required

Number of Pages Required

1 page

Colors
876aae
ec1f27
f37022
9bcb3c

Requirements
Must have
• Colorful pictures nature, brings out emotion, colorful, children from various parts of the world, animals.
• Tried to down load some pictures but would not go thru.

```html
<!DOCTYPE html>
<html lang="en">
<head>
<meta charset="utf-8">
<title>The Bright Meadow Foundation</title>
<link href="https://fonts.googleapis.com/css2?family=Fraunces:opsz,wght@9..144,300;9..144,400&family=Questrial&display=swap" rel="stylesheet">
<style>
:root{
  --purple:#876aae;
  --purple-light:#b9a5d9;
  --purple-btn:#9b7fd0;
  --red:#ec1f27;
  --orange:#f37022;
  --green:#9bcb3c;
  --green-dark:#5f8f16;
  --grey-block:#c9c9c9;
  --grey-bg:#f2f2f2;
  --ink:#222;
  --muted:#666;
  --line:#bdbdbd;
  --serif:'Fraunces',Georgia,serif;
  --sans:'Questrial',Arial,sans-serif;
}
*{margin:0;padding:0;box-sizing:border-box}
html,body{width:1200px;height:3338px;overflow:hidden;background:#fff}
body{position:relative;font-family:var(--sans);color:var(--ink)}
.abs{position:absolute}

/* header */
.site-header{position:absolute;left:0;top:0;width:1200px;height:91px;background:#fff}
.brand{position:absolute;left:126px;top:26px;display:flex;align-items:center;gap:8px}
.brand-dot{width:26px;height:26px;border-radius:50%;background:var(--purple)}
.brand-name{font-family:var(--serif);color:var(--purple);font-size:17px;line-height:1.05;letter-spacing:.5px}
.main-nav a{position:absolute;top:36px;font-size:16px;color:var(--ink);text-decoration:none}
.nav-caret{display:inline-block;margin-left:8px;border-left:5px solid transparent;border-right:5px solid transparent;border-top:8px solid var(--ink);vertical-align:middle}
.donate-btn{position:absolute;left:980px;top:31px;width:107px;height:31px;border:1.5px solid var(--green);color:var(--green);font-size:18px;text-align:center;line-height:28px}

/* hero */
.hero{position:absolute;left:0;top:91px;width:1200px;height:529px;background:linear-gradient(110deg,#5a3b2c 0%,#9a5a3e 25%,#7d3f6b 50%,#a8475a 70%,#6b4a58 100%)}
.hero-title{position:absolute;left:587px;top:240px;font-family:var(--serif);font-weight:300;font-size:54px;color:#fff}
.hero-text{position:absolute;left:594px;top:328px;width:470px;font-size:14px;line-height:21px;color:#fff}
.hero-btn{position:absolute;left:708px;top:421px;width:179px;height:40px;background:var(--purple-btn);color:#fff;font-size:18px;text-align:center;line-height:40px}
.social-rail .tile{position:absolute;left:1159px;width:41px;height:42px}

/* mission */
.mission-block{position:absolute}
.section-title{font-family:var(--serif);font-weight:300;color:var(--ink)}
.mission-title{position:absolute;left:113px;top:735px;font-size:31px}
.mission-text{position:absolute;left:113px;top:797px;width:504px;font-size:13.4px;line-height:21.2px;text-align:justify}
.pillar{position:absolute;top:1008px;width:160px;text-align:center}
.pillar span{display:block;margin-top:12px;font-size:19px}
.pillar-divider{position:absolute;top:1008px;width:1.5px;height:122px;background:#333}

/* partner */
.partner{position:absolute;left:0;top:1238px;width:1200px;height:513px;background:var(--grey-bg)}
.partner-title{position:absolute;left:522px;top:70px;font-size:31px}
.partner-sub{position:absolute;left:522px;top:152px;font-family:var(--serif);font-weight:300;font-size:21px}
.partner-text{position:absolute;left:522px;width:566px;font-size:13.4px;line-height:21.2px}

/* founders */
.card{position:absolute;overflow:hidden;border-radius:2px}
.card-photo{position:absolute;left:0;top:0;width:100%}
.card-info{position:absolute;left:0;bottom:0;width:100%;text-align:center;color:#fff}
.card-name{font-family:var(--serif);font-weight:300;font-size:21px;line-height:24px}
.card-role{font-family:var(--serif);font-weight:300;font-size:15px;line-height:16px}
.know-btn{display:block;margin:10px auto 0;width:153px;height:33px;font-family:var(--serif);font-size:15px;line-height:33px;color:#fff}
.founders-intro{background:var(--purple);color:#fff;text-align:center}
.founders-intro h2{font-family:var(--serif);font-weight:300;font-size:50px;line-height:44px;margin-top:120px}
.future{background:var(--green);color:#222;padding:18px 20px}
.future h3{font-family:var(--serif);font-weight:300;font-size:26px;text-align:center;margin-bottom:14px}
.future p{font-size:13.4px;line-height:21.2px}

.meadow{position:absolute;left:0;top:2440px;width:1200px;height:450px;background:linear-gradient(180deg,#ffffff 0%,#e7e9ee 22%,#b9c0cf 45%,#6e5cb8 70%,#4b3f8f 85%,#3f6b3a 100%)}

/* partners row */
.partner-name{position:absolute;top:2915px;font-size:34px;color:var(--ink);text-align:center;width:260px}

/* footer */
.rule{position:absolute;left:113px;width:976px;height:1.5px;background:var(--line)}
.foot-head{position:absolute;top:3035px;font-family:var(--serif);font-weight:300;font-size:17px}
.foot-links{position:absolute;top:3080px;list-style:none;font-size:13.5px;color:var(--muted);line-height:25px}
.foot-about{position:absolute;left:447px;top:3076px;width:305px;font-size:13.4px;line-height:19.5px;color:var(--muted);text-align:justify}
.contact-row{position:absolute;left:780px;display:flex;align-items:center;gap:22px;font-size:14.5px;color:var(--ink)}
.follow{position:absolute;left:113px;top:3224px;font-size:17px;display:flex;align-items:center;gap:14px}
.follow .sq{width:24px;height:24px;background:#777;border-radius:3px}
.copyright{position:absolute;right:111px;top:3220px;font-size:14px;display:flex;align-items:center;gap:8px}
.copyright .dot{width:22px;height:22px;border-radius:50%;background:var(--purple)}
.legal{position:absolute;right:111px;top:3248px;font-size:14px;word-spacing:2px}
</style>
</head>
<body>

<header class="site-header">
  <div class="brand">
    <div class="brand-dot"></div>
    <div class="brand-name">Bright Meadow<br>Foundation</div>
  </div>
  <nav class="main-nav">
    <a style="left:417px">About Us</a>
    <a style="left:517px">Projects</a>
    <a style="left:607px">Support Us</a>
    <a style="left:723px">Get Involved<span class="nav-caret"></span></a>
    <a style="left:862px">Contact Us</a>
  </nav>
  <div class="donate-btn">DONATE</div>
</header>

<section class="hero" role="img" aria-label="Photo of a smiling mother in a bright woven hat holding her young child">
  <h1 class="hero-title" style="top:149px">Pledge to Volunteer</h1>
  <p class="hero-text" style="top:237px">Creating a more comprehensivemedical team of volunteers and resources both from the United States as well other countries and from local &nbsp;communities is a component of the organization's long term goals.</p>
  <div class="hero-btn" style="top:330px">SUPPORT US</div>
  <svg class="abs" style="left:548px;top:431px" width="116" height="20" viewBox="0 0 116 20">
    <polygon points="12,3 12,17 2,10" fill="#fff"/>
    <circle cx="36" cy="10" r="6" fill="#fff"/>
    <circle cx="56" cy="10" r="5.5" fill="none" stroke="#fff" stroke-width="1.8"/>
    <circle cx="76" cy="10" r="5.5" fill="none" stroke="#fff" stroke-width="1.8"/>
    <polygon points="104,3 104,17 114,10" fill="#fff"/>
  </svg>
</section>

<div class="social-rail">
  <div class="tile" style="top:145px;background:var(--green)"></div>
  <div class="tile" style="top:192px;background:#3b5998"></div>
  <div class="tile" style="top:239px;background:#c13584"></div>
</div>

<!-- mission -->
<div class="mission-block" style="left:863px;top:620px;width:337px;height:618px;background:var(--grey-block)"></div>
<div class="mission-block" style="left:828px;top:667px;width:35px;height:528px;background:var(--purple-light)"></div>
<div class="mission-block" style="left:640px;top:783px;width:560px;height:326px;background:var(--purple)"></div>
<div class="mission-block" role="img" aria-label="Portrait of a woman in a bright orange and red embroidered headscarf with jewellery" style="left:661px;top:758px;width:461px;height:331px;background:linear-gradient(135deg,#c9542a,#e89a3c 40%,#b8332f 70%,#7a2a3a)"></div>

<h2 class="section-title mission-title">Our Mission</h2>
<p class="mission-text">The Bright Meadow Foundation was founded with the aim of helping rural and indigenous individuals in various parts of the world. The foundation’s vision is to see that every woman, man and child have access to basic medical care and treatment as well as fundamental knowledge in preventative care. There are many people living in regions of the world today who have limited or no access to health centers. Often, these individuals travel hours and in many instances days for basic care that often times can be averted with preventative care measures.</p>

<div class="pillar" style="left:105px">
  <svg width="80" height="66" viewBox="0 0 80 66"><path d="M40 62 C10 42 4 30 4 20 C4 10 12 3 22 3 C30 3 36 8 40 14 C44 8 50 3 58 3 C68 3 76 10 76 20 C76 30 70 42 40 62Z" fill="none" stroke="#222" stroke-width="2.5"/><polyline points="2,34 24,34 30,24 36,44 42,18 48,38 52,34 78,34" fill="none" stroke="var(--red)" stroke-width="2.5"/></svg>
  <span>Healthcare</span>
</div>
<div class="pillar-divider" style="left:266px"></div>
<div class="pillar" style="left:274px">
  <svg width="66" height="66" viewBox="0 0 66 66"><path d="M20 62 V50 C10 44 6 34 8 24 C10 10 22 3 34 3 C48 3 58 14 58 28 L62 38 H56 V48 H44 V62" fill="none" stroke="#222" stroke-width="2.5"/><circle cx="34" cy="26" r="8" fill="none" stroke="var(--green)" stroke-width="2.5"/><circle cx="22" cy="34" r="5" fill="none" stroke="#222" stroke-width="2"/></svg>
  <span>Knowledge</span>
</div>
<div class="pillar-divider" style="left:434px"></div>
<div class="pillar" style="left:436px">
  <svg width="60" height="66" viewBox="0 0 60 66"><path d="M30 3 L56 12 V32 C56 48 44 58 30 64 C16 58 4 48 4 32 V12Z" fill="none" stroke="#222" stroke-width="2.5"/><path d="M30 12 L47 18 V32 C47 43 39 50 30 54 C21 50 13 43 13 32 V18Z" fill="none" stroke="#222" stroke-width="2"/><path d="M26 24 H34 V30 H40 V38 H34 V44 H26 V38 H20 V30 H26Z" fill="none" stroke="var(--orange)" stroke-width="2.2"/></svg>
  <span>Prevention</span>
</div>

<!-- partner -->
<section class="partner">
  <svg class="abs" style="left:0;top:0" width="520" height="513" viewBox="0 0 520 513">
    <path d="M0 0 H282 C250 60 250 120 300 180 C360 260 380 330 380 400 C380 440 390 480 400 513 H0Z" fill="#c9e2a0"/>
    <path d="M0 0 H262 C232 60 232 125 282 185 C340 260 360 330 360 400 C360 440 370 480 378 513 H0Z" fill="url(#parrotTone)" role="img" aria-label="Photo of a red, green and blue macaw perched on a branch"/>
    <defs><linearGradient id="parrotTone" x1="0" y1="0" x2="1" y2="1"><stop offset="0" stop-color="#c8d9a8"/><stop offset=".4" stop-color="#c0392b"/><stop offset=".65" stop-color="#2a7fb8"/><stop offset="1" stop-color="#9a9a7a"/></linearGradient></defs>
  </svg>
  <h2 class="section-title partner-title">Partner with Us!</h2>
  <h3 class="partner-sub">We would love for you to partner with us on our endeavors!</h3>
  <p class="partner-text" style="top:190px">We welcome volunteers of all ages, abilities, and skill sets. If you are interested please contact us for more information.</p>
  <p class="partner-text" style="top:244px">Creating a more comprehensive medical team of volunteers and resources both from the United States as well other countries and from local communities is a component of the organization's long term goals. We seek to recruit and empower each community so that they become more selfsufficient with health and wellness issues. Our hope is to achieve this through classroom teaching and hands-on learning. Needs assessments are conducted in each community visited to assess the overall health at each location with the help and guidance of local community members. These assessments will include but are not limite &nbsp;to data gathering, looking at the overall health status, the regional health issues, morbidity and mortality reports, resource availability and nutrition.</p>
</section>

<!-- meadow backdrop -->
<div class="meadow" role="img" aria-label="Photo of purple lupine flowers in a misty mountain meadow"></div>

<!-- founders -->
<div class="card founders-intro" style="left:187px;top:1818px;width:263px;height:337px">
  <svg class="abs" style="left:101px;top:34px" width="62" height="62" viewBox="0 0 62 62"><circle cx="31" cy="31" r="30" fill="#fff"/></svg>
  <h2>Meet<br>Our<br>Founders</h2>
</div>

<div class="card" style="left:468px;top:1821px;width:266px;height:334px;background:var(--red)">
  <div class="card-photo" role="img" aria-label="Portrait photo of co-founder Dorla Penn" style="height:214px;background:linear-gradient(135deg,#d51a20,#8a1216 60%,#2f3f8a)"></div>
  <div class="card-info" style="height:120px;padding-top:14px">
    <div class="card-name">Dorla Penn, FNP</div>
    <div class="card-role">Co-Founder</div>
    <div class="know-btn" style="background:#c4000a">KNOW MORE</div>
  </div>
</div>

<div class="card" style="left:756px;top:1821px;width:264px;height:337px;background:var(--purple)">
  <div class="card-photo" role="img" aria-label="Portrait photo of co-founder Wade Marlow" style="height:212px;background:linear-gradient(135deg,#3a3ac9,#a63fd1 50%,#e04fc0)"></div>
  <div class="card-info" style="height:125px;padding-top:16px">
    <div class="card-name">Wade Marlow</div>
    <div class="card-role">Co-Founder</div>
    <div class="know-btn" style="background:var(--purple-btn)">KNOW MORE</div>
  </div>
</div>

<div class="card" style="left:184px;top:2197px;width:264px;height:321px;background:var(--orange)">
  <div class="card-photo" role="img" aria-label="Portrait photo of co-founder Marina Kellet" style="height:214px;background:linear-gradient(135deg,#8a9a6a,#4a4a44 55%,#b7b7b0)"></div>
  <div class="card-info" style="height:107px;padding-top:8px">
    <div class="card-name">Marina Kellet</div>
    <div class="card-role">Co-Founder</div>
    <div class="know-btn" style="background:#c8653a;margin-top:8px">KNOW MORE</div>
  </div>
</div>

<div class="card" style="left:468px;top:2197px;width:266px;height:321px;background:var(--green)">
  <div class="card-photo" role="img" aria-label="Portrait photo of co-founder Rosa Tembley" style="height:214px;background:linear-gradient(135deg,#cfe3a8,#b38a6a 50%,#9bcb3c)"></div>
  <div class="card-info" style="height:107px;padding-top:8px">
    <div class="card-name">Rosa Tembley FNP</div>
    <div class="card-role">Co-Founder</div>
    <div class="know-btn" style="background:var(--green-dark);margin-top:8px">KNOW MORE</div>
  </div>
</div>

<div class="card future" style="left:753px;top:2197px;width:266px;height:321px">
  <h3>Our Future</h3>
  <p>We are committed to investing in the health and welfare of our global community. The Foundation will continue to expand work into other rural areas of both Central and South America. In addition, We are currently working on a partnership with a nongovernmental organiza-tion in South Africa and hope to be expanding to this part of the globe in the near future.</p>
</div>

<!-- giving partners -->
<div class="partner-name" style="left:133px">ShopGive</div>
<div class="partner-name" style="left:472px">RaiseTogether</div>
<div class="partner-name" style="left:800px">FriendPage</div>

<div class="rule" style="top:2998px"></div>

<h4 class="foot-head" style="left:113px">Quick Links</h4>
<ul class="foot-links" style="left:113px"><li>About Us</li><li>Projects</li><li>Our Founders</li><li>Contact Us</li></ul>
<h4 class="foot-head" style="left:280px">Get Involved</h4>
<ul class="foot-links" style="left:282px"><li>Give a Donation</li><li>Volunteer</li><li>Corporate Support</li><li>Support Us</li></ul>
<h4 class="foot-head" style="left:447px">Support Us</h4>
<p class="foot-about">Your donations allow us to provide medical care, health resources and supplies, and wellness education to the communities we serve. The links below are some of the ways you can donate to our organization.</p>
<h4 class="foot-head" style="left:780px;top:3037px">Contact Us</h4>

<div class="contact-row" style="top:3086px">
  <svg width="22" height="22" viewBox="0 0 22 22"><circle cx="11" cy="11" r="10" fill="none" stroke="#777" stroke-width="1.3"/><path d="M7 6 L9 6 L10 9 L9 10 C10 12 11 13 13 13 L14 12 L17 13 L17 15 C12 16 6 10 7 6Z" fill="none" stroke="#777" stroke-width="1.2"/></svg>
  <span>1-555-014-2280</span>
</div>
<div class="contact-row" style="top:3111px">
  <svg width="22" height="22" viewBox="0 0 22 22"><rect x="2" y="5" width="18" height="12" fill="none" stroke="#777" stroke-width="1.3"/><polyline points="2,5 11,12 20,5" fill="none" stroke="#777" stroke-width="1.3"/></svg>
  <span>info@thebrightmeadowfoundation.org</span>
</div>
<div class="contact-row" style="top:3136px">
  <svg width="22" height="22" viewBox="0 0 22 22"><circle cx="11" cy="11" r="9.5" fill="none" stroke="#777" stroke-width="1.3"/><ellipse cx="11" cy="11" rx="4" ry="9.5" fill="none" stroke="#777" stroke-width="1.2"/><line x1="1.5" y1="11" x2="20.5" y2="11" stroke="#777" stroke-width="1.2"/></svg>
  <span>www. thebrightmeadowfoundation.org</span>
</div>

<div class="rule" style="top:3196px"></div>

<div class="follow"><span>Follow Us</span><div class="sq"></div><div class="sq"></div></div>
<div class="copyright"><span>Copyright 2020 The Bright Meadow Foundation.</span><div class="dot"></div><span>All rights reserved.</span></div>
<div class="legal">Terms of Service &nbsp;&nbsp; | &nbsp;&nbsp; Privacy &nbsp;&nbsp; | &nbsp;&nbsp; Legal notice</div>

</body>
</html>
```